The Gemstone Craft Studio Sales Business Card

The goal of this project is to create a interactive & effective business card design for SALES purposes with the intention to get customer on to our website and make a purchase or contact us about a product or service.
Website: WWW.RINGFORGEHUB.COM
GoogleMyBusiness: https://g.page/RingForgeHUB?gm
Facebook & Instagram: @THEGEMSTONECRAFTSTUDIO
Phone # & Text Message & Whatsapp Message: +1(555) 418-0293
Email: HELLO@RINGFORGEHUB.COM
Location: 4872 Brambleton Avenue Suite 512 Elmbrook, OH
(It would be necessary to have the appropriate ticker/icon for each social media platform as well as the location ticker and phone / messaging icons instead of spelling the words out.)
It is important to have the company logo and details but with an emphasis toward website. Feel free to also completely make one design your way and completely custom as you feel best.
The Gemstone Craft Studio is a Provider of Luxury Goods & Services such as: Custom Jewelry Design, Jewelry Repairs & Cleaning, Designer Jewelry, Luxury Gifts, 24 Karat Gold, 22 Karat Gold Jewelry, Diamond Jewelry, Insured Jewelry Appraisals, Loose Gemstones & Diamonds, Supporting Sustainability
Target Market(s)
People looking to invest in precious metals and gemstones as well as people looking to find a gift for a loved one for a special occasion. Customers looking to Custom Design Jewelry.
Contact Information for Business Card
Font styles to use
Other font styles liked:
- w.e you want
Colors
Designer to choose colors to be used in the design.
Requirements
Must have
- Website: WWW.RINGFORGEHUB.COM
- GoogleMyBusiness: https://g.page/RingForgeHUB?gm
- Facebook & Instagram: @THEGEMSTONECRAFTSTUDIO
- Phone # & Text Message & Whatsapp Message: +1(555) 418-0293
- Email: HELLO@RINGFORGEHUB.COM
- Location: 4872 Brambleton Avenue Suite 512 Elmbrook, OH
- (It would be necessary to have the appropriate ticker/icon for each social media platform as well as the location ticker and phone / messaging icons instead of spelling the words out.)
- It is important to have the company logo and details but with an emphasis toward website. Feel free to also completely make one design your way and completely custom as you feel best.
Nice to have
- The Gemstone Craft Studio is a Provider of Luxury Goods & Services such as: Custom Jewelry Design, Jewelry Repairs & Cleaning, Designer Jewelry, Luxury Gifts, 24 Karat Gold, 22 Karat Gold Jewelry, Diamond Jewelry, Insured Jewelry Appraisals, Loose Gemstones & Diamonds, Supporting Sustainability

```html
<!DOCTYPE html>
<html lang="en">
<head>
<meta charset="utf-8">
<title>The Gemstone Craft Studio – Business Card</title>
<link rel="stylesheet" href="https://fonts.googleapis.com/css2?family=Open+Sans:wght@400;600;700&display=swap">
<style>
  :root {
    --backdrop: #2b2b2b;
    --card-dark: #1f1f1f;
    --card-light: #ffffff;
    --brand-red: #e21f26;
    --brand-gold: #f5c518;
    --ink: #1a1a1a;
    --ink-light: #ffffff;
  }
  * { box-sizing: border-box; margin: 0; padding: 0; }
  html, body { width: 1200px; height: 1021px; overflow: hidden; }
  body {
    background: var(--backdrop);
    font-family: "Open Sans", Arial, sans-serif;
    position: relative;
  }
  .card {
    position: absolute;
    left: 220px;
    width: 760px;
    height: 434px;
    box-shadow: 0 12px 30px rgba(0,0,0,.45);
  }
  /* Back of card */
  .card--back {
    top: 52px;
    background: var(--card-dark);
    color: var(--ink-light);
    display: flex;
    flex-direction: column;
    align-items: center;
    justify-content: center;
    gap: 30px;
  }
  .brand { display: flex; align-items: center; gap: 14px; }
  .brand__mark { width: 22px; height: 22px; background: var(--brand-gold); flex: none; }
  .brand__name {
    color: var(--brand-red);
    font-weight: 700;
    font-size: 34px;
    letter-spacing: .5px;
  }
  .services {
    text-align: center;
    font-size: 17px;
    line-height: 1.55;
    padding: 0 20px;
  }
  .services__line { display: block; white-space: nowrap; }
  .services .dot { color: var(--brand-gold); margin: 0 3px; }

  /* Front of card */
  .card--front {
    top: 535px;
    background: var(--card-light);
    color: var(--ink);
  }
  .front__brand {
    position: absolute;
    left: 40px; top: 150px;
    width: 330px;
  }
  .front__brand .brand__name { font-size: 30px; line-height: 1.2; }
  .front__brand .brand { align-items: flex-start; }
  .front__brand .brand__mark { margin-top: 10px; }
  .address {
    position: absolute;
    left: 40px; bottom: 56px;
    display: flex; align-items: center; gap: 8px;
    font-size: 19px;
    white-space: nowrap;
  }
  .contacts {
    position: absolute;
    left: 410px; top: 70px;
    width: 320px;
  }
  .contact-group { padding: 14px 0; }
  .contact-group + .contact-group { border-top: 2px solid var(--brand-gold); }
  .contact-row {
    display: flex; align-items: center; gap: 10px;
    font-size: 18px; line-height: 1.55;
    white-space: nowrap;
  }
  .contact-row svg { flex: none; }
  .website { font-weight: 700; }
  .website .accent { color: var(--brand-red); }
  .social-mark { width: 16px; height: 16px; background: var(--brand-red); border-radius: 3px; flex: none; }
</style>
</head>
<body>

<section class="card card--back">
  <div class="brand">
    <span class="brand__mark"></span>
    <span class="brand__name">The Gemstone Craft Studio</span>
  </div>
  <p class="services">
    <span class="services__line">Custom Jewelry Design <span class="dot">•</span> Jewelry Repairs &amp; Cleaning <span class="dot">•</span> Designer Jewelry</span>
    <span class="services__line">Luxury Gifts <span class="dot">•</span> 24 Karat Gold <span class="dot">•</span> 22 Karat Gold Jewelry <span class="dot">•</span> Insured Jewelry Appraisals</span>
    <span class="services__line">Diamond Jewelry <span class="dot">•</span> Loose Gemstones &amp; Diamonds <span class="dot">•</span> Supporting Sustainability</span>
  </p>
</section>

<section class="card card--front">
  <div class="front__brand">
    <div class="brand">
      <span class="brand__mark"></span>
      <span class="brand__name">The Gemstone Craft Studio</span>
    </div>
  </div>

  <p class="address">
    <svg width="14" height="18" viewBox="0 0 14 18"><path d="M7 1a5.5 5.5 0 0 0-5.5 5.5C1.5 11 7 17 7 17s5.5-6 5.5-10.5A5.5 5.5 0 0 0 7 1z" fill="none" stroke="var(--brand-red)" stroke-width="2"/><circle cx="7" cy="6.5" r="2" fill="var(--brand-red)"/></svg>
    4872 Brambleton Avenue, Suite 512, Elmbrook, OH
  </p>

  <div class="contacts">
    <div class="contact-group">
      <p class="contact-row website">
        <svg width="16" height="16" viewBox="0 0 16 16" fill="none" stroke="var(--brand-red)" stroke-width="1.5"><circle cx="8" cy="8" r="7"/><ellipse cx="8" cy="8" rx="3" ry="7"/><path d="M1 8h14"/></svg>
        <span>www.<span class="accent">ringforgehub</span>.com</span>
      </p>
      <p class="contact-row">
        <svg width="16" height="16" viewBox="0 0 14 18"><path d="M7 1a5.5 5.5 0 0 0-5.5 5.5C1.5 11 7 17 7 17s5.5-6 5.5-10.5A5.5 5.5 0 0 0 7 1z" fill="none" stroke="var(--brand-red)" stroke-width="2"/></svg>
        g.page/RingForgeHUB?gm
      </p>
    </div>
    <div class="contact-group">
      <p class="contact-row"><span class="social-mark"></span>@thegemstonecraftstudio</p>
      <p class="contact-row"><span class="social-mark"></span>@thegemstonecraftstudio</p>
    </div>
    <div class="contact-group">
      <p class="contact-row">
        <svg width="16" height="16" viewBox="0 0 16 16"><path d="M3 1l3 3-2 2c1 2 4 5 6 6l2-2 3 3-2 2C7 15 1 9 1 3z" fill="var(--brand-red)"/></svg>
        +1(555) 418-0293
      </p>
      <p class="contact-row">
        <svg width="16" height="14" viewBox="0 0 16 14" fill="none" stroke="var(--brand-red)" stroke-width="1.6"><rect x="1" y="1" width="14" height="12"/><path d="M1 1l7 6 7-6"/></svg>
        hello@ringforgehub.com
      </p>
    </div>
  </div>
</section>

</body>
</html>
```